New Business card design to reflect rebrand

I would like a business card design with a good base colour for our new logo and also a placeholder for a profile pic of the card holder. the design needs to be editable to the point that we can easily change the picture of the person and use that design for printlarkly etc. we are looking at a metalic finish business card so will need a good base colour to bring out the finish.

Target Market(s)

prospective customers

Industry/Entity Type

Business

Contact Information for Business Card

I would like one editable design that we can change the name of the card holder and profile picture. The design need to be in a format that be send to printlarkly etc.

Our address is Fenwick Lodge, Mill Lane, Ashcombe Vale, KT14 3WB Tel no. 01632 960418

Requirements
Must have
• place holder for a profile pic for the card holder. in AI or preferably PSD format

```html
<!DOCTYPE html>
<html lang="en">
<head>
<meta charset="utf-8">
<title>Norvane Workplace Services – Business Card</title>
<link href="https://fonts.googleapis.com/css2?family=Open+Sans:wght@300;400;600;700&display=swap" rel="stylesheet">
<style>
  :root {
    --backdrop: #3b322c;
    --brand-orange: #c6521b;
    --brand-orange-deep: #ad4616;
    --brand-navy: #34506b;
    --card-white: #f0efeb;
    --ink-light: #ffffff;
    --panel-tint: rgba(255, 255, 255, 0.10);
  }
  * { margin: 0; padding: 0; box-sizing: border-box; }
  html, body {
    width: 1200px; height: 1200px; overflow: hidden;
    background: var(--backdrop);
    font-family: "Open Sans", Arial, sans-serif;
  }
  .sheet {
    width: 1200px; height: 1200px;
    display: flex; flex-direction: column; align-items: center; justify-content: center;
    gap: 80px;
  }
  .card {
    width: 760px; height: 430px; position: relative; overflow: hidden;
    box-shadow: 0 10px 28px rgba(0,0,0,0.35);
  }
  /* Back side */
  .card-back {
    background: linear-gradient(135deg, var(--brand-orange) 0%, var(--brand-orange-deep) 100%);
    color: var(--ink-light);
  }
  .details-panel {
    position: absolute; left: 22px; top: 96px; width: 430px; height: 312px;
    background: var(--panel-tint);
    padding: 34px 30px;
  }
  .holder-name {
    font-weight: 600; font-size: 30px; letter-spacing: 1px; text-transform: uppercase;
    line-height: 1.2;
  }
  .contact-list { margin-top: 52px; list-style: none; }
  .contact-item { margin-bottom: 20px; font-size: 19px; line-height: 1.35; font-weight: 600; }
  .contact-icon { display: block; width: 26px; height: 26px; margin-bottom: 6px; }
  .photo-slot {
    position: absolute; right: 0; top: 0; width: 308px; height: 100%;
    background: linear-gradient(160deg, #c4511c 0%, #b04816 100%);
    display: flex; align-items: center; justify-content: center;
  }
  .photo-label {
    transform: rotate(-90deg);
    font-size: 62px; font-weight: 300; letter-spacing: 10px;
    color: rgba(255,255,255,0.10);
  }
  /* Front side */
  .card-front {
    background: var(--card-white);
    display: flex; align-items: center; justify-content: center;
  }
  .brand-lockup { display: flex; align-items: center; gap: 22px; }
  .brand-dot { width: 26px; height: 26px; border-radius: 50%; background: var(--brand-orange); }
  .brand-name {
    color: var(--brand-navy); font-weight: 700; text-transform: uppercase;
    font-size: 48px; line-height: 1.1; letter-spacing: 3px;
  }
  .brand-name span { display: block; font-size: 26px; letter-spacing: 6px; }
</style>
</head>
<body>
<main class="sheet">
  <section class="card card-back" aria-label="Business card back">
    <div class="details-panel">
      <h1 class="holder-name">Card Holder Name</h1>
      <ul class="contact-list">
        <li class="contact-item">
          <svg class="contact-icon" viewBox="0 0 26 26" aria-hidden="true">
            <circle cx="13" cy="13" r="11.5" fill="none" stroke="#fff" stroke-width="2"/>
            <path d="M7 11c0-2 3-3.5 6-3.5s6 1.5 6 3.5l-2 .6-.6-1.8h-6.8l-.6 1.8z" fill="#fff"/>
            <rect x="8.5" y="12.5" width="9" height="5" rx="1" fill="none" stroke="#fff" stroke-width="1.6"/>
          </svg>
          01632 960418
        </li>
        <li class="contact-item">
          <svg class="contact-icon" viewBox="0 0 26 26" aria-hidden="true">
            <circle cx="13" cy="13" r="11.5" fill="none" stroke="#fff" stroke-width="2"/>
            <path d="M13 6.5a4.5 4.5 0 0 0-4.5 4.5c0 3.3 4.5 8 4.5 8s4.5-4.7 4.5-8A4.5 4.5 0 0 0 13 6.5z" fill="#fff"/>
            <circle cx="13" cy="11" r="1.7" fill="#c6521b"/>
          </svg>
          Fenwick Lodge, Mill Lane<br>Ashcombe Vale, KT14 3WB
        </li>
      </ul>
    </div>
    <div class="photo-slot" role="img" aria-label="Profile photo of the card holder">
      <span class="photo-label">PHOTO</span>
    </div>
  </section>

  <section class="card card-front" aria-label="Business card front">
    <div class="brand-lockup">
      <div class="brand-dot" aria-hidden="true"></div>
      <p class="brand-name">Norvane<span>Workplace Services</span></p>
    </div>
  </section>
</main>
</body>
</html>
```